Faithful Harbor Fellowship Network needs a fresh new web design

We are an up and coming multicultural church that aims to bring people into a life changing encounter with God. We need a fresh and inviting website in order to increase our internet presence and make us easier to connect with.
Here are some of the basic requirements for the site:
• Clearly displayed address, service times, and contact info
• A staff profile page
• An area for a calendar with upcoming events and their details
• Social media buttons
• Group pages for the different ministries (youth, children’s church, men, etc…)
• An area for donations and eCommerce
• A resources page for assorted media (podcasts, sermons, videos, etc.…)
• An area for prayer requests.

Industry/Entity Type

Church

```html
<!DOCTYPE html>
<html lang="en">
<head>
<meta charset="utf-8">
<title>Faithful Harbor Fellowship Network</title>
<link rel="stylesheet" href="https://fonts.googleapis.com/css2?family=Cinzel:wght@400;600&family=Montserrat:wght@400;500&family=Arimo:wght@400;700&family=Oswald:wght@400&display=swap">
<style>
  :root {
    --page-grey: #e9e9eb;
    --rule-grey: #c9c9cc;
    --ink: #2a2a2a;
    --soft-ink: #4a4a4a;
    --royal: #4312c6;
    --royal-deep: #34127e;
    --lilac: #7a55d0;
    --link-blue: #1a5fd6;
    --panel-grey: #e6e6e8;
    --white: #ffffff;
  }
  * { box-sizing: border-box; margin: 0; padding: 0; }
  html, body { width: 1200px; height: 815px; overflow: hidden; }
  body { position: relative; background: var(--white); font-family: "Arimo", Arial, sans-serif; color: var(--ink); }

  .site-header { position: absolute; left: 0; top: 0; width: 1200px; height: 145px; background: var(--page-grey); border-bottom: 1px solid var(--rule-grey); }
  .brand { position: absolute; left: 188px; top: 44px; display: flex; align-items: center; gap: 10px; }
  .brand-mark { width: 46px; height: 46px; border-radius: 50%; background: var(--royal-deep); flex: none; }
  .brand-name { font-family: "Montserrat", sans-serif; font-weight: 500; font-size: 17px; line-height: 21px; color: var(--royal-deep); width: 210px; }

  .social { position: absolute; left: 925px; top: 25px; display: flex; gap: 8px; }
  .social a { display: block; width: 24px; height: 24px; }
  .social .s1 { background: #2f5aa6; }
  .social .s2 { background: #2aa3e0; }
  .social .s3 { background: #e0513b; }

  .main-nav { position: absolute; right: 186px; top: 92px; font-family: "Montserrat", sans-serif; font-size: 13.5px; color: var(--ink); display: flex; gap: 0; }
  .main-nav a { color: var(--ink); text-decoration: none; }
  .main-nav .sep { margin: 0 9px; }

  .hero { position: absolute; left: 0; top: 145px; width: 1200px; height: 340px;
    background:
      linear-gradient(180deg, rgba(0,0,0,0) 72%, rgba(40,22,10,0.9) 92%, #20150c 100%),
      radial-gradient(ellipse at 45% 60%, #ffd860 0%, #f3a72a 35%, #c8691b 65%, #6e3410 100%); }
  .hero-title { position: absolute; left: 189px; top: 60px; font-family: "Cinzel", serif; font-weight: 600; font-size: 53px; letter-spacing: 1px; color: var(--royal); }
  .hero-sub { position: absolute; left: 189px; top: 118px; font-family: "Montserrat", sans-serif; font-size: 18.5px; color: #1c1208; }
  .hero-btn { position: absolute; left: 189px; top: 170px; width: 122px; height: 40px; background: var(--royal); color: var(--white); font-family: "Oswald", sans-serif; font-size: 21px; line-height: 40px; text-align: center; text-decoration: none; border-radius: 2px; letter-spacing: 0.3px; }

  .section-title { font-family: "Montserrat", sans-serif; font-weight: 400; font-size: 19px; color: var(--soft-ink); }

  .mission-icon { position: absolute; left: 200px; top: 519px; }
  .mission { position: absolute; left: 252px; top: 518px; width: 256px; }
  .mission p { margin-top: 9px; font-size: 10px; line-height: 17px; text-align: justify; color: var(--ink); }

  .divider { position: absolute; left: 543px; top: 519px; height: 155px; border-left: 1px dashed #8a8a8a; }

  .events-icon { position: absolute; left: 570px; top: 520px; }
  .events { position: absolute; left: 632px; top: 518px; width: 230px; }
  .event { margin-top: 10px; font-size: 10px; line-height: 17px; }
  .event strong { font-weight: 700; color: #111; }
  .events .more { display: block; margin-top: 10px; font-size: 10.5px; font-weight: 700; color: var(--link-blue); text-decoration: none; }

  .contact { position: absolute; left: 890px; top: 500px; width: 210px; height: 213px; background: var(--panel-grey); padding: 18px 0 0 21px; }
  .contact address { font-style: normal; margin-top: 14px; font-size: 11.5px; line-height: 17px; color: #333; }
  .contact .row { display: flex; align-items: center; gap: 12px; margin-top: 17px; font-size: 11.5px; color: #333; }

  .site-footer { position: absolute; left: 0; top: 731px; width: 1200px; height: 84px; background: var(--page-grey); border-top: 1px solid var(--rule-grey); }
  .site-footer p { position: absolute; left: 0; width: 1200px; top: 25px; text-align: center; font-size: 10.5px; color: #4a3a30; }
  .site-footer .gap { display: inline-block; width: 18px; }
</style>
</head>
<body>
  <header class="site-header">
    <div class="brand">
      <span class="brand-mark"></span>
      <span class="brand-name">Faithful Harbor Fellowship Network</span>
    </div>
    <nav class="social" aria-label="Social media">
      <a class="s1" href="#" aria-label="Social page one"></a>
      <a class="s2" href="#" aria-label="Social page two"></a>
      <a class="s3" href="#" aria-label="Social page three"></a>
    </nav>
    <nav class="main-nav">
      <a href="#">Home</a><span class="sep">|</span>
      <a href="#">Staff Profile</a><span class="sep">|</span>
      <a href="#">Ministries</a><span class="sep">|</span>
      <a href="#">Donations</a><span class="sep">|</span>
      <a href="#">Media</a>
    </nav>
  </header>

  <section class="hero" role="img" aria-label="Silhouette of a person with raised arms against a golden sunset sky over hills">
    <h1 class="hero-title">A HOUSE OF PRAYER</h1>
    <p class="hero-sub">experience the love, the presence, and the power of God</p>
    <a class="hero-btn" href="#">LEARN MORE</a>
  </section>

  <svg class="mission-icon" width="32" height="46" viewBox="0 0 32 46" aria-hidden="true">
    <rect x="11" y="0" width="9" height="46" fill="#7a55d0"/>
    <rect x="0" y="12" width="32" height="8" fill="#7a55d0"/>
  </svg>
  <section class="mission">
    <h2 class="section-title">Mission</h2>
    <p>We are a house of prayer that exists to create an uplifting atmosphere where people of all nations experience the love, the presence, and the power of God through the preaching and teaching of the Bible. We are a place where Jesus's work of redemption and the power of the Holy Spirit minister to the whole human being through adequate activities</p>
  </section>

  <div class="divider"></div>

  <svg class="events-icon" width="44" height="47" viewBox="0 0 44 47" aria-hidden="true">
    <rect x="2" y="6" width="40" height="39" rx="3" fill="none" stroke="#7a55d0" stroke-width="3.5"/>
    <rect x="2" y="6" width="40" height="10" fill="#7a55d0"/>
    <rect x="11" y="0" width="5" height="12" rx="2" fill="#7a55d0"/>
    <rect x="28" y="0" width="5" height="12" rx="2" fill="#7a55d0"/>
    <text x="22" y="39" text-anchor="middle" font-family="Arimo, sans-serif" font-weight="700" font-size="17" fill="#7a55d0">31</text>
  </svg>
  <section class="events">
    <h2 class="section-title">Events</h2>
    <div class="event"><strong>Event 1 will go here. Event 1 will go here</strong><br>June 19, 2014</div>
    <div class="event"><strong>Event 2 will go here</strong><br>June 19, 2014</div>
    <a class="more" href="#">Learn more &gt;&gt;</a>
  </section>

  <aside class="contact">
    <h2 class="section-title">Contact</h2>
    <address>Address will go here<br>Address will go here</address>
    <div class="row">
      <svg width="14" height="12" viewBox="0 0 14 12" aria-hidden="true"><path d="M1 4 Q7 -1 13 4 L11 5 L9 3.5 L5 3.5 L3 5 Z" fill="#666"/><rect x="3" y="6" width="8" height="6" rx="1" fill="#666"/></svg>
      <span>hello@faithfulharbor.org</span>
    </div>
    <div class="row">
      <svg width="14" height="11" viewBox="0 0 14 11" aria-hidden="true"><rect x="0.5" y="0.5" width="13" height="10" fill="#666"/><path d="M1 1 L7 6 L13 1" fill="none" stroke="#e6e6e8" stroke-width="1.2"/></svg>
      <span>+1 555-014-2290</span>
    </div>
  </aside>

  <footer class="site-footer">
    <p>Copyright 2014&nbsp; Faithful Harbor Fellowship Network<span class="gap"></span>Contact Us&nbsp; |&nbsp; Terms and Conditions</p>
  </footer>
</body>
</html>
```